Zielgruppe
Wir sind ein Landwirtschaftsbetrieb für Obstbau und unsere Kunden sind hauptsächlich Privatpersonen und Familien aus der Region sowie Kleinbetriebe wie z. B. regionale Shops.
Aufgabenstellung
Wir benötigen Flaschenetiketten für Fruchtsäfte (3 verschiedene Sorten: Marillennektar, Pfirsichnektar, Kirschennektar) für 0,75 und 0,25 Liter Flaschen und für Schnaps und Liköre (Marillen, Kirschen, Pfirsich, Zwetschke, Kriecherl).
Wir würden eine Vorderseite, die das Design und die Pflichtangaben enthält, bevorzugen.
Die Schrift der Pflichtangaben muss wie folgt ausgeführt werden: Etiketten bis 80 cm2 Kleinbuchstaben mind. 0,9 mm, ab 80 cm2 Kleinbuchstaben mind. 1,2 mm, Großbuchstaben immer mind. 2 mm, das Feld benötigt in etwa 3,5 x 7 cm Platz. Für das Design gibt es noch keine fixe Größe.
Bitte keine Fotos von 'echtem' Obst verwenden.

```html
<!DOCTYPE html>
<html lang="de">
<head>
<meta charset="utf-8">
<title>Nektar-Etiketten</title>
<link href="https://fonts.googleapis.com/css2?family=Lora:wght@700&family=Lato:wght@400;700&family=Kalam:wght@700&display=swap" rel="stylesheet">
<style>
  :root {
    --apricot: #c48a4c;
    --cherry: #b8403a;
    --leaf: #4a6a3e;
    --sage: #8a9c7a;
    --apricot-wash: #f6ece0;
    --cherry-wash: #f3e0dc;
    --address: #8e4a33;
    --paper: #ffffff;
  }
  * { box-sizing: border-box; margin: 0; padding: 0; }
  html, body { width: 1200px; height: 850px; overflow: hidden; background: var(--paper); }
  body { position: relative; font-family: "Lato", sans-serif; }

  .label {
    position: absolute;
    width: 379px;
    height: 675px;
    border: 6px solid var(--accent);
    background: var(--paper);
    overflow: hidden;
  }
  .label--apricot { left: 184px; top: 94px; --accent: var(--apricot); --wash: var(--apricot-wash); --box: var(--sage); --addr: var(--address); }
  .label--cherry { left: 656px; top: 92px; --accent: var(--cherry); --wash: var(--cherry-wash); --box: var(--cherry); --addr: var(--cherry); }

  .brand {
    position: absolute; top: 44px; left: 0; right: 0;
    display: flex; justify-content: center; align-items: center; gap: 7px;
    font-family: "Lato", sans-serif; font-weight: 700; font-size: 14px;
    letter-spacing: 1.5px; color: #2b2b2b;
  }
  .brand__dot { width: 12px; height: 12px; border-radius: 50%; background: var(--cherry); }

  .wash {
    position: absolute; left: 12px; right: 4px; top: 86px; height: 362px;
    background: radial-gradient(ellipse at 55% 50%, var(--wash) 60%, rgba(255,255,255,0) 100%);
  }

  .title {
    position: absolute; left: 31px; top: 98px;
    font-family: "Lora", serif; font-weight: 700;
    font-size: 56px; line-height: 58px;
  }
  .title__fruit { display: block; color: var(--accent); }
  .title__kind { display: block; color: var(--leaf); }

  .fruit-art {
    position: absolute; left: 32px; top: 220px; width: 290px; height: 222px;
    border-radius: 45% 50% 40% 45%;
  }
  .label--apricot .fruit-art { background: radial-gradient(ellipse at 55% 60%, #f1b36b 0%, #f3c28d 45%, #9cb98a 75%, rgba(255,255,255,0) 100%); }
  .label--cherry .fruit-art { background: radial-gradient(ellipse at 60% 65%, #c9303a 0%, #d9555a 45%, #8cb07a 75%, rgba(255,255,255,0) 100%); }

  .badge {
    position: absolute; left: 243px; top: 201px; width: 96px; height: 96px;
    border-radius: 50%; background: var(--leaf);
    display: flex; align-items: center; justify-content: center; text-align: center;
    font-family: "Kalam", cursive; font-weight: 700; font-size: 14px; line-height: 17px;
    color: #ffffff; transform: rotate(5deg);
  }

  .ingredients {
    position: absolute; left: 35px; top: 450px; width: 302px; height: 74px;
    border-radius: 4px; background: var(--box); color: #ffffff;
    padding: 12px 16px; font-size: 14.5px; line-height: 16.5px;
  }
  .ingredients strong { font-weight: 700; }

  .storage {
    position: absolute; left: 10px; right: 10px; top: 534px;
    text-align: center; color: var(--leaf); font-size: 14.5px; line-height: 14.8px;
  }
  .storage strong { font-weight: 700; }

  .producer {
    position: absolute; left: 0; right: 0; top: 606px;
    text-align: center; color: var(--addr); font-weight: 700; font-size: 12.5px;
  }

  .volume {
    position: absolute; right: 42px; top: 630px;
    color: var(--leaf); font-size: 22px;
  }
</style>
</head>
<body>

<article class="label label--apricot">
  <div class="brand"><span class="brand__dot"></span>OBSTBAU-LINDENHOF</div>
  <div class="wash"></div>
  <h1 class="title"><span class="title__fruit">Marillen-</span><span class="title__kind">Nektar</span></h1>
  <div class="fruit-art" role="img" aria-label="Aquarell-Illustration: Marillen mit Blättern, eine Hälfte mit Kern"></div>
  <div class="badge">Marillen<br>aus eigener<br>Produktion</div>
  <div class="ingredients"><strong>Zutaten:</strong> Wasser, Fruchtfleisch, Zucker, Säuerungsmittel: Zitronensäure, Antioxidationsmittel: Ascorbinsäure</div>
  <p class="storage"><strong>Mindestens haltbar:</strong> siehe Verschluss<br>Kühl und dunkel lagern; vor dem Öffnen<br>schütteln und innerhalb einiger Tage<br>konsumieren</p>
  <p class="producer">Martin Lindner, Am Anger 7, A-3120 Wiesenfeld</p>
  <p class="volume">e 0,75 l</p>
</article>

<article class="label label--cherry">
  <div class="brand"><span class="brand__dot"></span>OBSTBAU-LINDENHOF</div>
  <div class="wash"></div>
  <h1 class="title"><span class="title__fruit">Kirsch-</span><span class="title__kind">Nektar</span></h1>
  <div class="fruit-art" role="img" aria-label="Aquarell-Illustration: drei Kirschen mit Stielen und Blatt"></div>
  <div class="badge">Marillen<br>aus eigener<br>Produktion</div>
  <div class="ingredients"><strong>Zutaten:</strong> Wasser, Fruchtfleisch, Zucker, Säuerungsmittel: Zitronensäure, Antioxidationsmittel: Ascorbinsäure</div>
  <p class="storage"><strong>Mindestens haltbar:</strong> siehe Verschluss<br>Kühl und dunkel lagern; vor dem Öffnen<br>schütteln und innerhalb einiger Tage<br>konsumieren</p>
  <p class="producer">Martin Lindner, Am Anger 7, A-3120 Wiesenfeld</p>
  <p class="volume">e 0,75 l</p>
</article>

</body>
</html>
```